Grace-Rooted Harvest Church OL- Theme for 2022

We, Grace-Rooted Harvest Church of Oak Landing, need a design for a 4' x 6' banner that will be placed on two walls in the main sanctuary. The banner is to communicate/advertise the church's theme for 2022, "He Will Make All Things New: A New You - 2022" Revelations 21:5. The design should include our logo and church name. Use the color purple. We have not worshipped in our church building since 2020 due to the COVID pandemic. This banner should be reflective of change, newness as we plan to re-enter the building this spring. Our congregation demographic is 95% African American, 5% Hispanic. Our home base is Tampa, Florida (USA), but we have a large social media following, primarily due to the pandemic.

Target Market(s)

Church members, Ages 1-99; male and female

Industry/Entity Type

Religious

Font styles to use
Serif

Colors
0094D4
00A9DD
6FCCEA
C7EBF8
E9F6FB
00AB8E
00BBA5
67D7C9
C6EFE9
E9F9F6
6B429C
8869AF
B7A5CE
E3DAEB
F3F0F8

Requirements
Must have
• Theme, scripture, church logo and color purple

```html
<!DOCTYPE html>
<html lang="en">
<head>
<meta charset="UTF-8">
<title>Grace-Rooted Harvest Church of Oak Landing – 2022 Theme Banner</title>
<link rel="stylesheet" href="https://fonts.googleapis.com/css2?family=Montserrat:wght@800&family=Open+Sans:wght@300;400&family=Kaushan+Script&display=swap">
<style>
  :root {
    --sky-deep: #1f9bdc;
    --sky-mid: #3fb4e8;
    --sky-light: #c7ebf8;
    --cloud: #f3f8fc;
    --lavender: #e3daeb;
    --lilac: #cfc0e2;
    --title-blue: #0b78c4;
    --theme-purple: #6b429c;
    --page: #ffffff;
  }
  * { margin: 0; padding: 0; box-sizing: border-box; }
  html, body {
    width: 1200px;
    height: 960px;
    overflow: hidden;
    background: var(--page);
  }
  .canvas {
    position: relative;
    width: 1200px;
    height: 960px;
    background: var(--page);
  }
  .banner {
    position: absolute;
    left: 357px;
    top: 94px;
    width: 500px;
    height: 743px;
    overflow: hidden;
    box-shadow: 0 1px 3px rgba(0,0,0,0.12);
  }
  .sky-backdrop {
    position: absolute;
    inset: 0;
    background:
      radial-gradient(ellipse 60% 28% at 30% 12%, rgba(255,255,255,0.75), rgba(255,255,255,0) 70%),
      radial-gradient(ellipse 80% 30% at 55% 50%, rgba(255,255,255,0.95), rgba(255,255,255,0) 75%),
      radial-gradient(ellipse 55% 35% at 10% 80%, var(--lilac), rgba(207,192,226,0) 75%),
      radial-gradient(ellipse 70% 30% at 60% 90%, rgba(255,255,255,0.95), rgba(255,255,255,0) 75%),
      radial-gradient(ellipse 30% 40% at 100% 70%, var(--sky-deep), rgba(31,155,220,0) 80%),
      linear-gradient(180deg, var(--sky-mid) 0%, #4fb8e9 30%, var(--cloud) 55%, var(--lavender) 80%, #eef4fb 100%);
  }
  .church-mark {
    position: absolute;
    top: 120px;
    left: 0;
    right: 0;
    display: flex;
    flex-direction: column;
    align-items: center;
    gap: 10px;
  }
  .church-mark__dot {
    width: 56px;
    height: 56px;
    border-radius: 50%;
    background: var(--theme-purple);
  }
  .church-mark__name {
    font-family: "Open Sans", sans-serif;
    font-weight: 400;
    font-size: 17px;
    line-height: 1.25;
    color: var(--theme-purple);
    text-align: center;
    width: 300px;
  }
  .theme {
    position: absolute;
    left: 0;
    right: 0;
    text-align: center;
  }
  .theme__lead {
    top: 236px;
    font-family: "Montserrat", sans-serif;
    font-weight: 800;
    font-size: 58px;
    letter-spacing: -1px;
    color: var(--title-blue);
    line-height: 1;
  }
  .theme__sub {
    top: 294px;
    font-family: "Open Sans", sans-serif;
    font-weight: 300;
    font-size: 41px;
    letter-spacing: 3px;
    color: var(--title-blue);
    line-height: 1;
  }
  .theme__headline {
    top: 330px;
    font-family: "Kaushan Script", cursive;
    font-size: 104px;
    color: var(--theme-purple);
    line-height: 1.2;
  }
  .theme__year {
    top: 465px;
    font-family: "Montserrat", sans-serif;
    font-weight: 800;
    font-size: 58px;
    color: var(--title-blue);
    line-height: 1;
  }
  .theme__scripture {
    top: 541px;
    font-family: "Open Sans", sans-serif;
    font-weight: 400;
    font-size: 22px;
    letter-spacing: 3px;
    color: var(--title-blue);
    line-height: 1;
  }
</style>
</head>
<body>
  <main class="canvas">
    <section class="banner">
      <div class="sky-backdrop" role="img" aria-label="Bright blue sky with soft white and lavender clouds, sun rays and birds in flight"></div>

      <div class="church-mark">
        <span class="church-mark__dot"></span>
        <p class="church-mark__name">Grace-Rooted Harvest Church of Oak Landing</p>
      </div>

      <h1 class="theme theme__lead">HE WILL MAKE</h1>
      <p class="theme theme__sub">ALL THINGS NEW:</p>
      <p class="theme theme__headline">A New You</p>
      <p class="theme theme__year">-2022</p>
      <p class="theme theme__scripture">REVELATIONS 21:5</p>
    </section>
  </main>
</body>
</html>
```